Need Business Card for our Indian Grocery Store

Industry/Entity Type

Grocery Store

Contact Information for Business Card

Manoj Baweja
Director

Store Locations:

Kingsbrook
482 Elm Parade
P: 03 9172 5843

Westmoor
613 Carlow Road
P: 03 9238 6014

email: kvtmarts@mailnest.example

Requirements
Must have
• Our logo Colours

```html
<!DOCTYPE html>
<html lang="en">
<head>
<meta charset="utf-8">
<title>KVT Marts – Business Card</title>
<link href="https://fonts.googleapis.com/css2?family=Lato:wght@400;700;900&display=swap" rel="stylesheet">
<style>
  :root {
    --brand-red: #e11f26;
    --card-white: #ffffff;
    --backdrop: #2a2a2e;
    --text-on-red: #ffffff;
  }
  * { box-sizing: border-box; margin: 0; padding: 0; }
  html, body {
    width: 1200px; height: 800px; overflow: hidden;
    background: var(--backdrop);
    font-family: "Lato", Arial, sans-serif;
  }
  .canvas {
    position: relative; width: 1200px; height: 800px;
    display: flex; align-items: center; justify-content: center; gap: 60px;
  }
  .card {
    position: relative; width: 520px; height: 298px;
    background: var(--card-white);
    box-shadow: 0 12px 30px rgba(0,0,0,.45);
    overflow: hidden;
  }
  .brand {
    display: flex; align-items: center; gap: 12px;
    color: var(--brand-red); font-weight: 900;
    letter-spacing: .02em; white-space: nowrap;
  }
  .brand-mark {
    display: block; background: var(--brand-red); border-radius: 50%;
  }
  .card-front { display: flex; align-items: center; justify-content: center; }
  .card-front .brand { font-size: 44px; }
  .card-front .brand-mark { width: 34px; height: 34px; }

  .card-back { display: flex; }
  .card-back .logo-side {
    width: 44%; display: flex; align-items: center; justify-content: center;
  }
  .card-back .brand { font-size: 30px; gap: 9px; }
  .card-back .brand-mark { width: 22px; height: 22px; }
  .card-back .info-side {
    width: 56%; background: var(--brand-red); color: var(--text-on-red);
    padding: 52px 22px 0 30px;
  }
  .person-name { font-size: 19px; font-weight: 700; line-height: 1.1; }
  .person-role { font-size: 14px; font-weight: 400; margin-bottom: 22px; }
  .location { margin-bottom: 12px; }
  .location-name { font-size: 13px; font-weight: 700; line-height: 1.3; }
  .contact-line {
    display: flex; align-items: center; gap: 6px;
    font-size: 13px; line-height: 1.3; white-space: nowrap;
  }
  .contact-line svg { flex: none; width: 10px; height: 12px; fill: var(--text-on-red); }
  .contact-line.email { margin-top: 6px; }
  .contact-line.email svg { width: 12px; height: 10px; }
</style>
</head>
<body>
<main class="canvas">
  <section class="card card-front" aria-label="Business card front">
    <div class="brand"><span class="brand-mark"></span>KVT Marts</div>
  </section>

  <section class="card card-back" aria-label="Business card back">
    <div class="logo-side">
      <div class="brand"><span class="brand-mark"></span>KVT Marts</div>
    </div>
    <div class="info-side">
      <p class="person-name">Manoj Baweja</p>
      <p class="person-role">Director</p>

      <div class="location">
        <p class="location-name">Kingsbrook</p>
        <p class="contact-line">
          <svg viewBox="0 0 10 12" aria-hidden="true"><path d="M5 0a4 4 0 0 0-4 4c0 3 4 8 4 8s4-5 4-8a4 4 0 0 0-4-4zm0 5.6A1.6 1.6 0 1 1 5 2.4a1.6 1.6 0 0 1 0 3.2z"/></svg>
          482 Elm Parade | 03 9172 5843
        </p>
      </div>

      <div class="location">
        <p class="location-name">Westmoor</p>
        <p class="contact-line">
          <svg viewBox="0 0 10 12" aria-hidden="true"><path d="M5 0a4 4 0 0 0-4 4c0 3 4 8 4 8s4-5 4-8a4 4 0 0 0-4-4zm0 5.6A1.6 1.6 0 1 1 5 2.4a1.6 1.6 0 0 1 0 3.2z"/></svg>
          613 Carlow Road | 03 9238 6014
        </p>
      </div>

      <p class="contact-line email">
        <svg viewBox="0 0 12 10" aria-hidden="true"><path d="M0 0h12v10H0zM1 1.2v.3l5 3.6 5-3.6v-.3zM1 2.7V9h10V2.7L6 6.3z"/></svg>
        kvtmarts@mailnest.example
      </p>
    </div>
  </section>
</main>
</body>
</html>
```